■目的・概要 ・QLSへの出稿用バナー作成をしていただける方を募集します。 ---------------- ■注意点 ご提案頂きましたバナー案について、SNSへの投稿・Webサイトへのアップ等を行わないようにお願いします。 ※承諾頂ける方のみコンペへの参加をお願いします。 ---------------- ■依頼詳細 ・バナー内にテキストを挿入する場合は、テキストレイヤーで挿入してください。 ・テキストはおよそ1/4サイズで表示される事を考慮して制作して下さい。 ・配信時は制作したバナーがスマホの画面幅程度に縮小されて表示されます。テキストの可読性を考慮して制作お願いします ・バナー広告を見て、押したくなるようなバナー作成をお願いします。 【重要な指定】 【1】 宣伝広告したい内容 ・建売住宅(注文住宅、自由設計ではない) 【2】訴求ポイント ・地域密着 ・3000万円代から物件 ・緑区販売棟数「地域ビルダー部門」11年連続シェア№1(2008年度~2018年度㈱街並動向調査室調べ) ・50年以上の販売実績 ・ソラティグループ 【3】訴求したいターゲット ・名古屋市緑区で新築住宅(建売)購入を検討している(注文住宅、自由設計ではない) ・30~40代のファミリー ・価格4000~6000万円を検討 【4】画像素材指定の無 https://solati-kmx-ieyado.jp/house/ 上記サイトより転用ください。 【5】バナー制作要望 ・清潔感のあるバナーにしてほしい。 ・インパクトの強いバナーでお願いします。 ・【2】の訴求ポイントをわかりやすく伝えられるバナーにしてください。 ※このコンペは最大3件採用予定です。多数のバナーのご提案お待ちしております。 ■ 参考サイト(配信サイト) https://solati-kmx-ieyado.jp/house/ ※対応方法の一部変更(9/27内容修正) ・コンペは今まで通り、1200×628 で行います。 ・採用になった作品の納品時に300×300のバナーを作成して頂き一緒に納品して頂きたいです ※300×300のバナーは採用バナーの簡易版としてつけて頂けると幸いです。 ⇒そのまま縮小というより、「メイン画像+社名(ロゴ)+一言キャッチ」くらい簡易的でOKです。 小さいバナーですので可読性を考慮して頂けると幸いです。 ■サイズと枚数 【コンペ】 ・1200 x 628 ・1枚 【納品時】 ・1200 x 628 → 1枚 ・300×300→ 1枚 ■納品ファイル ・フォトショップ形式(.psd) ■注意点・禁止事項 土日・祝日は対応することができません。 平日は9~18時までにご連絡いただければ、当日。 それ以降は翌日にご返信いたします。 ※Zumio QLSガイドラインに沿った内容である事 QLS掲載ガイドライン関連資料(http://adsinfo.zumio.co.jp/online/doc/pdf_guideline.html) ※他で登録されているデザインや商標の転用など、他社の知的財産権を侵すこと ※他のクライアントへ既に提案した内容の転用など たくさんのウェブデザイナーの方からのご提案をお待ちしております。 |
どの案もよかったのですが、今回はこちらのバナーを特に気に入りました。
みなさんバナーの提案ありがとうございます。また依頼する際もどうぞよろしくお願いします。

```html
<!DOCTYPE html>
<html lang="ja">
<head>
<meta charset="UTF-8">
<title>建売住宅 バナー</title>
<link rel="stylesheet" href="https://fonts.googleapis.com/css2?family=M+PLUS+Rounded+1c:wght@700;800&family=Noto+Sans+JP:wght@500;700;900&display=swap">
<style>
  :root {
    --navy: #1d3a86;
    --navy-deep: #15296a;
    --band: rgba(22, 40, 100, 0.92);
    --white: #ffffff;
    --circle: rgba(255, 255, 255, 0.9);
    --accent: #f08a1c;
    --night-top: #0e1a3a;
    --night-mid: #2c3f6e;
    --night-glow: #8a7a5a;
  }
  * { margin: 0; padding: 0; box-sizing: border-box; }
  html, body { width: 1200px; height: 628px; overflow: hidden; background: #fff; }
  .banner {
    position: relative;
    width: 1200px;
    height: 628px;
    overflow: hidden;
    font-family: "Noto Sans JP", sans-serif;
    color: var(--white);
  }
  .photo { position: absolute; }
  .photo--night-exterior {
    left: 0; top: 0; width: 1200px; height: 310px;
    background: linear-gradient(180deg, var(--night-top) 0%, var(--night-mid) 60%, var(--night-glow) 100%);
  }
  .photo--facade-gray {
    left: 0; top: 300px; width: 380px; height: 328px;
    background: linear-gradient(160deg, #cfd6df 0%, #7d8692 55%, #4f5862 100%);
  }
  .photo--living-room {
    left: 380px; top: 300px; width: 450px; height: 328px;
    background: linear-gradient(160deg, #f3ece2 0%, #d9c8b0 60%, #a88f70 100%);
  }
  .photo--facade-white {
    left: 830px; top: 300px; width: 370px; height: 328px;
    background: linear-gradient(160deg, #dfe7ee 0%, #c4ccd2 55%, #8a958e 100%);
  }
  .lead {
    position: absolute; top: 16px; left: 0; width: 100%;
    text-align: center;
    font-size: 27px; font-weight: 700; letter-spacing: 1px;
    text-shadow: 0 2px 4px rgba(0,0,0,0.5);
  }
  .label {
    position: absolute; left: 50%; top: 92px; transform: translateX(-50%);
    width: 260px; height: 58px;
    background: var(--navy);
    border: 3px solid var(--white);
    border-radius: 10px;
    display: flex; align-items: center; justify-content: center;
    font-size: 34px; font-weight: 900; letter-spacing: 4px;
  }
  .points {
    position: absolute; top: 218px; left: 0; width: 100%;
    list-style: none;
  }
  .point {
    position: absolute; top: 0;
    width: 190px; height: 190px; border-radius: 50%;
    background: var(--circle);
    display: flex; align-items: center; justify-content: center;
    text-align: center;
    font-family: "M PLUS Rounded 1c", sans-serif;
    font-weight: 800; font-size: 31px; line-height: 1.25;
    color: var(--navy-deep);
  }
  .point:nth-child(1) { left: 105px; }
  .point:nth-child(2) { left: 395px; }
  .point:nth-child(3) { left: 629px; }
  .point:nth-child(4) { left: 845px; }
  .record {
    position: absolute; left: 0; top: 498px; width: 100%; height: 86px;
    background: var(--band);
  }
  .record__main {
    position: absolute; left: 22px; top: 8px;
    display: flex; align-items: center; gap: 10px;
    font-size: 33px; font-weight: 900; white-space: nowrap;
  }
  .record__highlight {
    background: var(--white); color: var(--navy-deep);
    border-radius: 24px; padding: 0 20px; line-height: 46px;
    font-size: 33px;
  }
  .record__icon { width: 50px; height: 46px; }
  .record__note {
    position: absolute; left: 0; width: 100%; top: 58px;
    text-align: center; font-size: 20px; font-weight: 500;
  }
</style>
</head>
<body>
<main class="banner">
  <div class="photo photo--night-exterior" role="img" aria-label="夜景にライトアップされたモダンな建売住宅の外観"></div>
  <div class="photo photo--facade-gray" role="img" aria-label="グレーの外壁の住宅外観と植栽"></div>
  <div class="photo photo--living-room" role="img" aria-label="明るい木目調のリビング・ダイニングの室内"></div>
  <div class="photo photo--facade-white" role="img" aria-label="白い外壁の住宅外観と庭の植栽"></div>

  <p class="lead">名古屋市緑区で新築住宅（建売）購入を検討している方へ</p>
  <h1 class="label">建売住宅</h1>

  <ul class="points">
    <li class="point">地域密着</li>
    <li class="point">3000万円代<br>から</li>
    <li class="point">販売実績<br>50年以上</li>
    <li class="point">ソラティ<br>グループ</li>
  </ul>

  <section class="record">
    <div class="record__main">
      <span>緑区販売棟数「地域ビルダー部門」</span>
      <span class="record__highlight">１１年連続シェア№１</span>
      <svg class="record__icon" viewBox="0 0 50 46" aria-hidden="true">
        <path d="M6 20 L30 6 L34 34 L10 30 Z" fill="var(--accent)"/>
        <rect x="4" y="19" width="8" height="12" rx="2" fill="var(--accent)"/>
        <line x1="38" y1="10" x2="46" y2="4" stroke="var(--accent)" stroke-width="3" stroke-linecap="round"/>
        <line x1="40" y1="20" x2="48" y2="20" stroke="var(--accent)" stroke-width="3" stroke-linecap="round"/>
        <line x1="38" y1="30" x2="46" y2="36" stroke="var(--accent)" stroke-width="3" stroke-linecap="round"/>
      </svg>
    </div>
    <p class="record__note">（2008年度～2018年度㈱街並動向調査室調べ）</p>
  </section>
</main>
</body>
</html>
```